Kolibri-Stube
Ich bin sehr zufrieden mit dem Flyer, Plakat und Logo, welches ich für einen zahlbaren Preis bekommen habe. quorvix hat die Korrekturvorschläge sehr gut und immer zügig umgesetzt und ein wirklich gelungenes Resultat produzier.
Zielgruppe
Logo/Sloagan: Kolibri-Stube
Branchen: Kunst/Kultur und Bildung
Ich biete eine Kolibri-Stube an, in der bis 12 Personen quartalsweise über ein Jahr hinweg an einer Erzählung ode einem Roman arbeiten. Das Genre kann frei gewählt werden. Ob Kriminal-, Fantasy oder Liebesroman, Autobiografie oder Dokufiktion, die Grundlagen eines spannenden Textes sind die selben.
Zielgruppe sind Jugendliche bis Senioren, die gerne eine lägere Erzählung oder einen Roman schreiben möchten.
Aufgabenstellung
Siehe Design-Briefing (PDF) mit Inhalt für Flyertext
Wichtig ist mir der Flyer A4 gefaltet (zu A5 oder 2x gefaltet) oder A5, alle beidseits bedruckt und je nachdem, wie sie den Inhalt verteilen möchten.
Ich bin offen für Design- und Formatvorschläge.
- Ein Plakat A4/A3, welches mit der Vorderseite des Flyers grösstenteils übereinstimmt. Wenn ich ein InDesign oder Photoshop mit Layern kriege, kann ich den Text des Plakats selber ergänzen/bearbeiten.
Ich habe neben dem Briefing und einem Foto von mir noch ein paar Bilder hochgeladen, deren Stil mir gefällt. Habe aber NICHT deren Rechte. Bilder müssten also durch Sie gefunden werden, ich kann diese aber extra bezahlen, bitte Preis dafür deklarieren.
Logo brauche ich noch keines.
Besten Dank für Ihre Bemühungen

```html
<!DOCTYPE html>
<html lang="de">
<head>
<meta charset="utf-8">
<title>Kolibri-Stube – Flyer</title>
<link rel="stylesheet" href="https://fonts.googleapis.com/css2?family=Yanone+Kaffeesatz:wght@200;300;400;700&display=swap">
<style>
  :root {
    --wine: #460000;
    --wine-text: #7c0000;
    --gold: #f0c400;
    --rose: #e0c0c0;
    --white: #ffffff;
    --ink: #111111;
    --rule: #6a1a1a;
  }
  * { box-sizing: border-box; margin: 0; padding: 0; }
  html, body { width: 849px; height: 1200px; overflow: hidden; background: var(--white); }
  body { font-family: "Yanone Kaffeesatz", "Arial Narrow", sans-serif; color: var(--ink); }
  .sheet { position: relative; width: 849px; height: 1200px; border: 1px solid #000; overflow: hidden; background: var(--white); }
  .abs { position: absolute; }

  /* Blocks */
  .band { position: absolute; background: var(--wine); }
  .fold { position: absolute; width: 1px; background: var(--rule); }
  .sheet-divider { position: absolute; left: 0; top: 598px; width: 849px; height: 6px; background: #000; }
  .gold-line { position: absolute; height: 2px; background: var(--gold); }
  .gold-vline { position: absolute; width: 2px; background: var(--gold); }

  /* Outside: headline */
  .headline { position: absolute; left: 110px; top: 62px; width: 216px; text-align: center; color: var(--wine-text);
    text-shadow: 4px 5px 6px rgba(150, 0, 0, .35); line-height: 73px; font-size: 60px; }
  .headline .thin { font-weight: 200; display: block; }
  .headline .bold { font-weight: 700; display: block; }
  .url-front { position: absolute; left: 138px; top: 528px; font-size: 21px; font-weight: 400; color: var(--wine-text); }

  /* Cover */
  .name-card { position: absolute; left: 491px; top: 68px; width: 272px; height: 414px; background: var(--white);
    box-shadow: 3px 4px 6px rgba(0,0,0,.35); }
  .name-card .brand { position: absolute; left: 28px; top: 40px; font-size: 74px; font-weight: 400; line-height: 80px; color: var(--ink); }
  .quill { position: absolute; left: 550px; top: 351px; width: 237px; height: 169px;
    background: linear-gradient(160deg, #f3cc1a, #e8b800); border-radius: 60% 40% 50% 10%; }
  .tagline { position: absolute; left: 572px; top: 494px; width: 192px; color: var(--white); font-size: 24px; font-weight: 400;
    line-height: 30px; text-align: justify; text-align-last: justify; letter-spacing: .3px; }

  /* Inside */
  .questions { position: absolute; left: 96px; top: 682px; width: 230px; font-size: 13px; font-weight: 300; line-height: 16.5px; }
  .questions p { margin-bottom: 11px; }
  .questions b { font-weight: 400; }
  .note { position: absolute; background: var(--rose); padding: 3px 5px; font-size: 9.6px; font-weight: 300; line-height: 12.1px;
    text-align: justify; color: var(--ink); }
  .quote { position: absolute; left: 93px; top: 985px; width: 235px; color: #f1e2e2; font-size: 14px; font-weight: 200; line-height: 16.3px; }
  .quote b { font-weight: 400; color: var(--white); }
  .quote .sig { display: block; font-size: 6px; line-height: 10px; font-weight: 300; }
  .topics ul { list-style: none; margin-top: 11px; }
  .topics li { position: relative; padding-left: 9px; }
  .topics li::before { content: "·"; position: absolute; left: 0; }
  .quill-faint { position: absolute; left: 444px; top: 957px; width: 371px; height: 146px;
    background: radial-gradient(ellipse at 60% 45%, rgba(130,10,10,.35), rgba(90,0,0,0) 70%); }
  .url-back { position: absolute; left: 541px; top: 1005px; font-size: 29px; font-weight: 300; color: var(--white); letter-spacing: .3px; }
  .lead { position: absolute; left: 545px; top: 1083px; width: 220px; font-size: 9.6px; font-weight: 300; line-height: 12.2px;
    color: #f0dede; text-align: justify; }
  .lead b { font-weight: 400; color: var(--white); }
</style>
</head>
<body>
<main class="sheet">

  <!-- Outside spread -->
  <div class="band" style="left:0;top:0;width:115px;height:322px"></div>
  <div class="band" style="left:309px;top:323px;width:540px;height:275px"></div>
  <div class="fold" style="left:424px;top:323px;height:275px"></div>

  <div class="gold-line" style="left:50px;top:16px;width:324px"></div>
  <div class="gold-vline" style="left:50px;top:16px;height:50px"></div>
  <div class="gold-line" style="left:553px;top:16px;width:247px"></div>
  <div class="gold-vline" style="left:798px;top:16px;height:50px"></div>
  <div class="gold-line" style="left:50px;top:583px;width:324px"></div>
  <div class="gold-vline" style="left:372px;top:535px;height:50px"></div>
  <div class="gold-line" style="left:474px;top:583px;width:327px"></div>
  <div class="gold-vline" style="left:473px;top:132px;height:453px"></div>

  <h1 class="headline">
    <span class="thin">Ihr</span>
    <span class="bold">geistiger</span>
    <span class="bold">Schatz</span>
    <span class="thin">in Form</span>
    <span class="thin">eines</span>
    <span class="bold">Buches</span>
  </h1>
  <div class="url-front">www.kolibri-stube.ch</div>

  <div class="name-card">
    <div class="brand">Kolibri-<br>Stube</div>
  </div>
  <div class="quill" role="img" aria-label="Goldene Schreibfeder als Illustration"></div>
  <p class="tagline">Mit der Kolibri-Stube zu Ihrem eigenen Roman</p>

  <div class="sheet-divider"></div>

  <!-- Inside spread -->
  <div class="band" style="left:0;top:921px;width:849px;height:279px"></div>
  <div class="fold" style="left:424px;top:921px;height:279px"></div>

  <div class="gold-line" style="left:50px;top:616px;width:750px"></div>
  <div class="gold-vline" style="left:50px;top:616px;height:50px"></div>
  <div class="gold-vline" style="left:798px;top:616px;height:50px"></div>
  <div class="gold-line" style="left:50px;top:1183px;width:326px"></div>
  <div class="gold-vline" style="left:374px;top:1135px;height:50px"></div>
  <div class="gold-line" style="left:476px;top:1183px;width:320px"></div>
  <div class="gold-vline" style="left:476px;top:1135px;height:50px"></div>

  <section class="questions">
    <p>Haben Sie eine erste <b>Idee</b> für eine<br>Erzählung oder einen Roman?</p>
    <p>Eine lebhafte <b>Fantasie</b> für das Ausserordentliche<br>oder <b>ungewöhnlich Gewöhnliche?</b></p>
    <p>Oder ein <b>reiches Leben,</b> aus dessen Quelle Sie für<br>Ihre Geschichte schöpfen können?</p>
    <p>Und möchten Sie den zukünftigen Leserinnen und<br>Lesern <b>Ihren geistigen Schatz in Form eines Buches</b><br>schenken?</p>
  </section>

  <div class="note" style="left:89px;top:905px;width:228px;height:54px">Dann schreiben Sie Ihren ersten eigenen Roman!<br>Ein erster Ideenfaden spinnt sich in Ihren Gedanken und vielleicht haben Sie diesen schon zu Papier gebracht. Aber Sie wissen nicht wie fortfahren?</div>

  <div class="quote">Ich helfe Ihnen weiter!<br>Denn die <b>Schreibkunst fusst wie alle Künste nicht nur auf Genie, sondern in erster Linie auf Handwerk, dass Ich Ihnen beibringen kann.</b><span class="sig">Dr. Lena Varholt</span></div>

  <div class="note" style="left:89px;top:1090px;width:228px;height:66px">Sie selber lesen gerne und sind dem Schreiben nicht abgewandt. Eine perfekte Rechtschreibung ist nicht nötig, dafür gibt es das gegenseitige Lektorat. Aber sie sollten der deutschen Sprache soweit mächtig sein, dass Sie Haupt, Nebensätze, Fälle und Zeiten meistens korrekt anwenden.</div>

  <div class="note topics" style="left:541px;top:647px;width:228px;height:198px;text-align:left;padding-top:5px">Die Themen eines ganzen Jahres sind
    <ul>
      <li>Kreative Übungen für den Start des Schreibprozesses</li>
      <li>Schreibspiele, um Blockaden zu lösen</li>
      <li>Bestimmung des Genres und des Stils</li>
      <li>Entwicklung der Handlung und Spannung</li>
      <li>Wahl einer Erzählperspektive und der passenden Sprache</li>
      <li>Lebendige Protagonisten, Antagonisten und Nebenfiguren</li>
      <li>Dramatische Szenen durch Emotionen</li>
      <li>Gliederung des Stoffes zu einem roten Faden</li>
      <li>Lineare und nonlineare Erzählformen</li>
      <li>Eine Dreiaktstruktur mit interessanten Spannungsbögen</li>
      <li>Korrekturen des Stils und der Grammatik</li>
      <li>Stilistische, rhetorische und literarische Mittel</li>
      <li>Autobiografische Verfremdung und Wahrhaftigkeit</li>
      <li>Die Schnittmenge zwischen Leben und Fiktion</li>
    </ul>
  </div>

  <div class="note" style="left:541px;top:855px;width:228px;height:52px">Ein regelmässiger Austausch in Kleingruppen und im Plenum helfen Ihnen, Ihre Arbeit gegenseitig zu überdenken, zu korrigieren und zu erweitern. Verschiedene Textformen und exemplarische Beispiele aus der Literatur und dem Film bieten Impulse für den eigenen Text.</div>

  <div class="note" style="left:541px;top:917px;width:228px;height:30px">Ein eigener Laptop mit WLAN ist von Vorteil, da wir uns damit online leicht austauschen können.</div>

  <div class="quill-faint" role="img" aria-label="Blasse Schreibfeder als Hintergrundillustration"></div>
  <div class="url-back">www.kolibri-stube.ch</div>

  <p class="lead">Kursleitung<br><b>Dr. Lena Varholt</b> ist Erwachsenenbildnerin und Lehrerin für Deutsch und spezialisierte sich auf den Unterricht des literarischen Schreibens von Drehbücher, Erzählungen und Romanen. Als Autorin mehrerer Fachbücher und Verlagsleiterin des Feldmoos-Verlags kennt Sie auch die Möglichkeiten des Vertriebes und Buchhandels.</p>

</main>
</body>
</html>
```